Invitation - Photos with Santa

We’re doing an event this Christmas for people get photos with Santa.
It’ll be a postcard that we mail to people we know.
Size: 5 x 7, two sided
Details for back of postcard:
Saturday, December 4
10 a.m. - 12 p.m.
18457 Colvin Ln.
Strongsville, OH 44873
The company putting it on is Brightwick. I’ve got a million logo formats so just let me know what you need.
In terms of theme/look/feel for the front of card, I’m a little stuck so I’m open to whatever.
-Skip the line?
-Private Santa party?
-Screw the mall?
Attached is an old one we used last time time we did it.
Let me know if there are any questions!
People I know personally, people with kids, people who private photo with Santa without having to go to the mall

```html
<!DOCTYPE html>
<html lang="en">
<head>
<meta charset="utf-8">
<title>Brightwick – Selfie with Santa Postcard</title>
<link href="https://fonts.googleapis.com/css2?family=Kaushan+Script&family=Caveat+Brush&family=Montserrat:wght@500&display=swap" rel="stylesheet">
<style>
  :root{
    --stage:#c9c9c9;
    --orange:#e85c22;
    --orange-soft:#f08a5d;
    --red:#d40c0f;
    --ink:#0d0d0d;
    --white:#ffffff;
    --mist:#e4e4e4;
    --photo-warm:#b88a6e;
    --photo-deep:#6e2a22;
  }
  *{margin:0;padding:0;box-sizing:border-box}
  html,body{width:739px;height:1200px;overflow:hidden;background:var(--stage)}
  .postcard{position:absolute;left:59px;overflow:hidden;background:var(--white)}
  .postcard--front{top:135px;width:615px;height:439px;background:linear-gradient(135deg,#f4f4f4,var(--mist))}
  .postcard--back{top:657px;width:628px;height:449px}
  .layer{position:absolute;left:0;top:0}
  .front-photo{position:absolute;left:0;top:0;width:440px;height:439px;
    background:linear-gradient(120deg,#7d5a3e 0%,var(--photo-warm) 35%,#e9e2e6 55%,var(--photo-deep) 85%)}
  .headline{position:absolute;font-family:"Kaushan Script",cursive;color:var(--ink);line-height:1;white-space:nowrap}
  .headline--selfie{left:350px;top:30px;font-size:50px}
  .headline--with{left:398px;top:96px;font-size:46px}
  .headline--santa{left:392px;top:146px;font-size:74px}
  .balloon-date{position:absolute;left:212px;top:26px;width:124px;text-align:center;
    font-family:"Caveat Brush",cursive;color:var(--ink);font-size:29px;line-height:.95}
  .balloon-date .day{font-size:44px;display:block;margin-top:2px}
  .brand{position:absolute;display:flex;align-items:center;gap:6px;white-space:nowrap;
    font-family:"Montserrat",sans-serif;font-weight:500;color:var(--orange);letter-spacing:.3px}
  .brand__dot{width:10px;height:10px;border-radius:50%;background:var(--orange);flex:none}
  .brand--front{left:446px;top:385px;font-size:17px}
  .brand--back{left:160px;top:132px;font-size:17px}
  .back-photo{position:absolute;left:0;top:0;width:147px;height:449px;
    background:linear-gradient(180deg,#3f5a3a 0%,#a86e50 40%,#b52a22 65%,#8a8079 100%)}
  .details{position:absolute;left:355px;font-family:"Caveat Brush",cursive;color:var(--ink);font-size:24px;line-height:27px;white-space:nowrap}
  .details--time{top:20px}
  .details--place{top:126px}
  .stamp-box{position:absolute;left:550px;top:10px;width:67px;height:67px;border:2px solid var(--orange-soft)}
  .mail-divider{position:absolute;left:147px;top:200px;width:481px;border-top:1px dashed var(--orange-soft)}
</style>
</head>
<body>

<section class="postcard postcard--front" aria-label="Postcard front">
  <div class="front-photo" role="img" aria-label="Photo of a child and Santa by a Christmas tree, with a hand holding a phone taking their selfie"></div>
  <svg class="layer" width="615" height="439" viewBox="0 0 615 439" aria-hidden="true">
    <path d="M313 0 H615 V222 Q600 232 568 240 L578 292 L525 262 Q470 292 410 283 Q400 250 400 200 Q380 150 360 80 Z" fill="var(--orange)"/>
    <path d="M410 285 Q470 294 525 264 L578 292 L566 240 Q598 232 615 222" fill="none" stroke="var(--red)" stroke-width="1.5"/>
    <ellipse cx="272" cy="78" rx="64" ry="76" fill="var(--red)"/>
    <path d="M268 153 L276 153 L272 162 Z" fill="var(--red)"/>
  </svg>
  <div class="balloon-date">Saturday,<br>December<span class="day">4</span></div>
  <div class="headline headline--selfie">Get a selfie</div>
  <div class="headline headline--with">with</div>
  <div class="headline headline--santa">Santa</div>
  <div class="brand brand--front"><span class="brand__dot"></span>BRIGHTWICK</div>
</section>

<section class="postcard postcard--back" aria-label="Postcard back">
  <div class="back-photo" role="img" aria-label="Photo of Santa standing beside a decorated Christmas tree and gifts, pointing to the right"></div>
  <svg class="layer" width="628" height="449" viewBox="0 0 628 449" aria-hidden="true">
    <path d="M0 298 Q40 320 40 370 Q90 370 120 400 Q150 420 158 449 H0 Z" fill="var(--red)"/>
    <circle cx="331" cy="42" r="11" fill="none" stroke="var(--orange)" stroke-width="2.5"/>
    <path d="M331 35 V43 L337 47" fill="none" stroke="var(--orange)" stroke-width="2.5" stroke-linecap="round"/>
    <path d="M331 152 Q317 135 317 127 A14 14 0 0 1 345 127 Q345 135 331 152 Z" fill="var(--red)"/>
    <circle cx="331" cy="127" r="3.5" fill="var(--white)"/>
    <circle cx="331" cy="151" r="9" fill="none" stroke="var(--orange)" stroke-width="1.8"/>
  </svg>
  <div class="brand brand--back"><span class="brand__dot"></span>BRIGHTWICK</div>
  <div class="details details--time">Saturday,<br>December 4<br>10 a.m. - 12 p.m.</div>
  <div class="details details--place">18457 Colvin Ln.<br>Strongsville, OH 44873</div>
  <div class="stamp-box"></div>
  <div class="mail-divider"></div>
</section>

</body>
</html>
```